Quenby Computers Customer Acquisition Flyer

I need a flyer design for Quenby Computers which is aimed at acquiring new customers. They will be distributed in a letterbox drop and as handouts.

The design should communicate our ability to aid both consumer and small business with all their IT needs and wants, that we have all tools and skills to assist them. It would look modern, professional with a design on the bolder side of the scale.

Very little text to go on flyer, its more about letting people know who we are, wand what we do.

We do:
Computer hardware / software installation and troubleshooting
Custom built computers
Internet installations / WiFi set up
Network installation and consultation
Computer IT Security
Cloud Computing experts
Certified Torvan phone technicians.

not all of that needs to be on flyer, but if is an computer or connected to a computer / network, we can help you.

I have no preference on colours apart from logo which should not be changed.

If anyone require any more information to create a flyer, just ask me, as i am not sure how much information is needed.

Flyer should be in A5 format.

Target Market(s)

consumer and small business (1-50 employees)

Industry/Entity Type

Computer Repair

Requirements
Must have
• Clear easy to read text, graphics that convey us as the professionals we are.
• Logo with tag line, Your local IT specialists
• Contact details:
• Mobile: 0479 612 304
• Email: support@quenbycomputers.com.au
• Web: www.quenbycomputers.com.au
• Be in A5 format
Nice to have
• contact details like mobile to really stand out along with logo.
Should not have
• Go wild, you should not restrict too much the creative people out there.

```html
<!DOCTYPE html>
<html lang="en">
<head>
<meta charset="utf-8">
<title>Quenby Computers – Your Local IT Specialists</title>
<link rel="stylesheet" href="https://fonts.googleapis.com/css2?family=Anton&family=Cormorant+SC:wght@700&family=Arimo:wght@700&display=swap">
<style>
  :root {
    --brand-red: #e3232b;
    --deep-red: #b8141c;
    --paper: #ffffff;
    --soft-grey: #e9e9ec;
    --ink: #141414;
    --link-blue: #1d3fbf;
    --photo-warm: #c98f76;
    --photo-cool: #6f7f93;
  }
  html, body { margin: 0; padding: 0; overflow: hidden; }
  body { width: 849px; height: 1200px; background: var(--paper); }
  .flyer {
    position: relative;
    width: 849px;
    height: 1200px;
    overflow: hidden;
    background: var(--paper);
  }
  .flyer__backdrop { position: absolute; inset: 0; }
  .brand-name {
    position: absolute;
    top: 22px;
    left: 0;
    width: 100%;
    text-align: center;
    margin: 0;
    font-family: "Anton", sans-serif;
    font-weight: 400;
    font-size: 84px;
    line-height: 1;
    letter-spacing: 1px;
    color: var(--paper);
    text-transform: uppercase;
  }
  .hero-photo {
    position: absolute;
    left: 113px;
    top: 142px;
    width: 637px;
    height: 522px;
    background: linear-gradient(135deg, #f1e4dc 0%, var(--photo-warm) 35%, #8d6a60 60%, var(--photo-cool) 100%);
  }
  .tagline {
    position: absolute;
    left: 128px;
    top: 500px;
    margin: 0;
    font-family: "Anton", sans-serif;
    font-weight: 400;
    font-size: 72px;
    line-height: 1.0;
    color: var(--paper);
    -webkit-text-stroke: 2px var(--ink);
    paint-order: stroke fill;
    transform: skewX(-6deg);
    letter-spacing: 1px;
  }
  .services {
    position: absolute;
    top: 742px;
    left: 0;
    width: 100%;
    margin: 0;
    padding: 0;
    list-style: none;
    text-align: center;
    font-family: "Cormorant SC", serif;
    font-weight: 700;
    font-size: 36px;
    line-height: 53px;
    color: var(--ink);
  }
  .contact {
    position: absolute;
    top: 1110px;
    left: 0;
    width: 100%;
    text-align: center;
    font-family: "Arimo", sans-serif;
    font-weight: 700;
    font-size: 19px;
    line-height: 22px;
    color: var(--ink);
  }
  .contact__title { margin: 0; }
  .contact__line { margin: 0; }
  .contact__link { color: var(--link-blue); text-decoration: underline; }
</style>
</head>
<body>
<main class="flyer">
  <svg class="flyer__backdrop" width="849" height="1200" viewBox="0 0 849 1200" aria-hidden="true">
    <rect x="0" y="0" width="849" height="720" fill="var(--brand-red)"/>
    <path d="M0 40 C 70 200, 90 420, 0 620 Z" fill="var(--paper)" opacity="0.9"/>
    <path d="M0 110 C 50 260, 55 420, 0 540 Z" fill="var(--soft-grey)"/>
    <path d="M849 0 L849 260 C 800 170, 760 80, 700 0 Z" fill="var(--paper)" opacity="0.9"/>
    <path d="M0 700 C 250 640, 600 640, 849 560 L849 1200 L0 1200 Z" fill="var(--paper)"/>
    <path d="M0 700 C 250 640, 600 640, 849 560 L849 600 C 600 680, 250 690, 0 730 Z" fill="var(--soft-grey)"/>
    <path d="M610 1200 C 720 1120, 790 1040, 849 960 L849 1200 Z" fill="var(--soft-grey)"/>
  </svg>

  <h1 class="brand-name">Quenby Computers</h1>

  <div class="hero-photo" role="img" aria-label="Photo of hands typing on a laptop keyboard"></div>

  <p class="tagline">Your Local<br>IT specialists</p>

  <ul class="services">
    <li>Computer hardware / software installations</li>
    <li>Internet installations/WiFi setup</li>
    <li>Network installations consultation</li>
    <li>Computer IT security</li>
    <li>Cloud computing experts</li>
    <li>Certified Torvan phone technicians</li>
  </ul>

  <address class="contact" style="font-style: normal;">
    <p class="contact__title">Contact</p>
    <p class="contact__line">Mobile: 0479 612 304</p>
    <p class="contact__line">Email: <span class="contact__link">support@quenbycomputers.com.au</span></p>
    <p class="contact__line">Web: www.quenbycomputers.com.au</p>
  </address>
</main>
</body>
</html>
```